Graphic works

Brief 1.
An Overview / Background of the Business & Services-
It is a new business being set up. Our business is to design a solution to enable Alumni of higher institutions in Nigeria apply for their academic transcript through our system. the name of our product will be Record Relay Nigeria. We need logo, site banner, advert banner and several academic images. See www.rvq-ng.example for more insight.
The Target Market / Audience you are trying to reach-
Alumni of Nigeria Universities, usually between the ages of 20-40.
Design Specifics; any preferences or ideas for Style, Colour, Imagery, etc-
Color scheme will be several shades of light blue and white. Please check www.rvq-ng.example for more insight.

Brief 2

Pantrybasket.example is an online food and grocery shop, we supply fresh food stuff and other daily essential needs on request to customers. The site is already up (www.pantrybasket.example). We need logo, site rolling banner, advert banner and several offer graphics as shown in the placeholder images in the site now.
Working women in Nigeria.
Color scheme will be several shades of light Green and White. Please check the site.

Colors
e9f1ce
33b7a4
add136
9bcb3c

```html
<!DOCTYPE html>
<html lang="en">
<head>
<meta charset="utf-8">
<title>Pantry Basket – Fresh Food &amp; Groceries</title>
<link href="https://fonts.googleapis.com/css2?family=Open+Sans:wght@400;600;700&display=swap" rel="stylesheet">
<style>
:root{
  --teal:#33b7a4;
  --green:#9bcb3c;
  --lime:#add136;
  --pale:#e9f1ce;
  --ink:#333333;
  --muted:#777777;
  --line:#dddddd;
  --dark:#232323;
  --footer:#3b3b3b;
  --footer-base:#262626;
  --white:#ffffff;
}
*{box-sizing:border-box;margin:0;padding:0}
html,body{width:1200px;height:2244px;overflow:hidden;background:var(--white)}
body{position:relative;font-family:"Open Sans",Arial,sans-serif;color:var(--ink)}
a{color:inherit;text-decoration:none}
.abs{position:absolute}

/* header */
.brand{left:99px;top:22px;display:flex;align-items:center;gap:14px}
.brand-mark{width:90px;height:90px;border-radius:50%;background:var(--green)}
.brand-name{font-size:40px;font-weight:600;color:var(--teal);line-height:1}
.brand-tagline{font-size:12px;color:var(--muted);margin-top:6px}
.top-links{right:100px;top:32px;font-size:13px;color:#555;display:flex;gap:8px}
.top-links span.sep{color:#aaa}
.mini-cart{left:760px;top:72px;display:flex;align-items:center;gap:8px}
.mini-cart .count{text-align:right;font-size:14px;line-height:1.15;color:var(--teal)}
.mini-cart .count small{display:block;font-size:12px;color:#555}
.mini-cart .bag{width:34px;height:34px;background:var(--teal);display:flex;align-items:center;justify-content:center}
.search{left:880px;top:72px;width:220px;height:36px;display:flex}
.search .field{flex:1;background:var(--pale);font-size:14px;color:#666;padding:9px 14px}
.search .go{width:41px;background:var(--green);display:flex;align-items:center;justify-content:center}

/* nav */
.main-nav{left:0;top:147px;width:1200px;height:49px;background:var(--teal)}
.main-nav ul{position:absolute;left:99px;top:0;display:flex;list-style:none;height:49px}
.main-nav li{font-size:16px;font-weight:600;color:var(--white);padding:0 20px;line-height:49px}
.main-nav li.active{background:var(--green);padding:0 21px}

/* hero */
.hero{left:0;top:196px;width:1200px;height:458px;background:linear-gradient(100deg,#8fae4a 0%,#c9d79a 35%,#e7c39f 50%,#b9c889 70%,#7f9e3a 100%)}
.hero-arrow{top:193px;width:56px;height:72px;background:rgba(60,60,60,.45);display:flex;align-items:center;justify-content:center}
.caption-title{left:99px;top:334px;width:250px;height:52px;background:rgba(30,30,30,.85);color:var(--white);font-size:30px;line-height:52px;padding-left:14px}
.caption-sub{left:99px;top:390px;width:188px;height:41px;background:var(--teal);color:var(--white);font-size:17px;line-height:41px;padding-left:14px}
.promo{padding:18px 18px;color:var(--white)}
.promo-dark{left:797px;top:15px;width:303px;height:172px;background:var(--dark)}
.promo-green{left:797px;top:193px;width:303px;height:241px;background:var(--green)}
.promo h2{font-size:27px;font-weight:700;line-height:1.1;text-transform:uppercase}
.promo-green h2{font-size:28px;color:#2a2a2a;line-height:1.15}
.promo p{font-size:16px;margin:10px 0 12px}
.promo-green p{color:#2a2a2a;margin:8px 0 26px}
.btn-small{display:inline-block;font-size:11px;font-weight:600;color:var(--white);background:var(--green);border-radius:4px;padding:4px 10px}
.promo-green .btn-small{background:var(--dark)}
.promo-art{position:absolute;border-radius:8px}

/* sidebar */
.sidebar{left:99px;top:690px;width:241px}
.side-title{font-size:24px;color:var(--teal);padding-bottom:8px;border-bottom:3px solid var(--teal)}
.cat-list{list-style:none}
.cat-list li{height:37.5px;border-bottom:1px solid var(--line);font-size:15px;color:#555;padding:9px 14px;position:relative}
.cat-list li.has-sub::after{content:"";position:absolute;right:12px;top:17px;border:5px solid transparent;border-top-color:#aaa}
.side-btn{height:43px;background:var(--green);color:var(--white);font-size:21px;display:flex;align-items:center;gap:10px;padding-left:14px;margin-top:11px}
.side-btn:first-of-type{margin-top:26px}
.side-offer{height:243px;margin-top:10px;background:linear-gradient(180deg,#c9c2b2 0%,#6d6a67 55%,#3a3f4a 100%);position:relative}
.side-offer .badge{position:absolute;left:0;top:0;width:54px;height:44px;background:#fbf3d4;color:#d33b2a;font-weight:700;font-size:20px;font-style:italic;padding:6px 0 0 4px}
.side-offer .text{position:absolute;left:18px;bottom:10px;color:var(--white);font-size:31px;line-height:1.05}
.side-offer .text span{display:block;padding-left:60px}
.side-title.spaced{margin-top:40px}
.mini-product{display:flex;gap:12px;padding:22px 0 18px;border-bottom:1px solid var(--line)}
.mini-thumb{width:67px;height:58px}
.mini-info{font-size:14px;color:var(--ink)}
.mini-info .price{font-size:12px;color:var(--teal);margin:2px 0 4px}

/* main column */
.main{left:361px;top:691px;width:739px}
.section-head{display:flex;justify-content:space-between;align-items:center;height:36px}
.section-head h2{font-size:24px;font-weight:400;color:var(--ink)}
.next-btn{width:26px;height:33px;background:#d4d4d4;display:flex;align-items:center;justify-content:center}
.product-grid{display:grid;grid-template-columns:repeat(3,240px);column-gap:9.5px;row-gap:21px;margin-top:3px}
.product-card{text-align:center;height:199px}
.product-photo{height:141px}
.product-name{font-size:15px;color:var(--ink);margin-top:13px}
.product-price{font-size:13px;color:var(--teal);margin-top:2px}
.offer-strip{display:grid;grid-template-columns:366px 365px;gap:8px;margin-top:40px;height:105px}
.offer-tile{position:relative;color:var(--white);padding:8px 14px}
.offer-tile h3{font-size:29px;font-weight:400;line-height:1.1}
.offer-tile p{font-size:16px;font-weight:700;line-height:1.3}
.offer-ship{background:linear-gradient(90deg,#4b4f55,#80858b)}
.offer-call{background:linear-gradient(90deg,#3d8a2c,#6fae3c 55%,#c58a3c)}
.featured{margin-top:46px}
.featured .product-grid{margin-top:0}
.wide-banner{left:359px;top:1804px;width:741px;height:96px;background:linear-gradient(90deg,#1b1b1b 0%,#2a2a2a 45%,#1e1e1e 80%,#7a3a22 100%);color:var(--white)}
.wide-banner .art{position:absolute;left:0;top:0;width:150px;height:96px;background:linear-gradient(90deg,#6f4b2a,#2a2218)}
.wide-banner .line{position:absolute;left:252px;top:16px;font-size:20px}
.wide-banner .line b{font-size:27px;font-weight:600;color:var(--lime)}
.wide-banner .cta{position:absolute;left:527px;top:49px;background:var(--green);border-radius:4px;font-size:13px;font-weight:700;padding:6px 10px 6px 8px;display:flex;align-items:center;gap:6px}

/* footer */
.site-footer{left:0;top:1927px;width:1200px;height:254px;background:linear-gradient(180deg,#444 0%,var(--footer) 100%);color:#c9c9c9}
.footer-col{position:absolute;top:32px}
.footer-col h4{font-size:15px;font-weight:600;color:var(--white);margin-bottom:12px}
.footer-col ul{list-style:none;font-size:12.5px;line-height:25px}
.footer-col.nav-menu ul{columns:2;column-gap:0;width:230px}
.socials{position:absolute;left:133px;top:186px;display:flex;gap:6px}
.socials span{width:28px;height:28px;background:var(--white);border-radius:3px;display:flex;align-items:center;justify-content:center}
.payments{position:absolute;left:423px;top:189px;display:flex;gap:12px}
.payments span{width:42px;height:27px;background:var(--white);border-radius:2px;font-size:9px;font-weight:700;color:#2a4a8a;display:flex;align-items:center;justify-content:center}
.copyright{left:0;top:2181px;width:1200px;height:63px;background:var(--footer-base);color:#aaa;font-size:12px;text-align:center;line-height:63px}
</style>
</head>
<body>

<header>
  <a class="abs brand" href="#">
    <span class="brand-mark"></span>
    <span>
      <span class="brand-name">Pantry Basket</span>
      <span class="brand-tagline" style="display:block">Feed well, live well</span>
    </span>
  </a>
  <nav class="abs top-links">
    <a href="#">MY ACCOUNT</a><span class="sep">/</span>
    <a href="#">MY WISHLIST</a><span class="sep">/</span>
    <a href="#">MY CART</a><span class="sep">/</span>
    <a href="#">CHECKOUT</a><span class="sep">/</span>
    <a href="#">LOG IN</a>
  </nav>
  <div class="abs mini-cart">
    <div class="count">0 items<small>$00.00</small></div>
    <div class="bag">
      <svg width="20" height="18" viewBox="0 0 20 18"><path d="M1 6h18l-2 11H3z" fill="#fff"/><path d="M6 6l4-5 4 5" stroke="#fff" stroke-width="2" fill="none"/></svg>
    </div>
  </div>
  <div class="abs search">
    <div class="field">Search</div>
    <div class="go"><svg width="18" height="18" viewBox="0 0 18 18"><circle cx="7.5" cy="7.5" r="5.5" stroke="#fff" stroke-width="2.4" fill="none"/><path d="M11.5 11.5l5 5" stroke="#fff" stroke-width="2.6"/></svg></div>
  </div>
</header>

<nav class="abs main-nav">
  <ul>
    <li class="active">HOME</li>
    <li>HEALTH &amp; WELLNESS</li>
    <li>FRUITS &amp; VEGS</li>
    <li>POULTRY, MEAT &amp; FISH</li>
    <li>FOOD STUFFS</li>
    <li>RECIPES</li>
    <li>OTHERS</li>
  </ul>
</nav>

<section class="abs hero" role="img" aria-label="Rolling banner photo: smiling woman holding a red apple on a sunny green lawn">
  <div class="abs hero-arrow" style="left:0"><svg width="16" height="30" viewBox="0 0 16 30"><path d="M14 2L2 15l12 13" stroke="#fff" stroke-width="2" fill="none"/></svg></div>
  <div class="abs hero-arrow" style="left:1143px;width:57px"><svg width="16" height="30" viewBox="0 0 16 30"><path d="M2 2l12 13L2 28" stroke="#fff" stroke-width="2" fill="none"/></svg></div>
  <div class="abs caption-title">Premium Quality</div>
  <div class="abs caption-sub">Fresh fruit every day</div>
  <div class="abs promo promo-dark">
    <h2>Free Delivetry &amp;<br>Get 10% Discount</h2>
    <p>Every Registered Users</p>
    <span class="btn-small">Read More</span>
    <div class="promo-art" role="img" aria-label="Yellow price tag illustration" style="left:228px;top:92px;width:50px;height:50px;background:#f3b521;transform:rotate(20deg)"></div>
  </div>
  <div class="abs promo promo-green">
    <h2>Herbal &amp;<br>Ayurvedic &amp; Spa<br>Products</h2>
    <p>Aliquam erat volutpat</p>
    <span class="btn-small">Read More</span>
    <div class="promo-art" role="img" aria-label="Mortar and pestle illustration" style="left:222px;top:172px;width:62px;height:50px;background:#1c1c1c;border-radius:0 0 30px 30px"></div>
  </div>
</section>

<aside class="abs sidebar">
  <h3 class="side-title" style="font-weight:400">Categories</h3>
  <ul class="cat-list">
    <li>All</li>
    <li>Health &amp; Wellness</li>
    <li class="has-sub">Fruits &amp; Vegs</li>
    <li class="has-sub">Poultry, Meat &amp; Fish</li>
    <li class="has-sub">Food Stuffs</li>
    <li>Recipes</li>
    <li class="has-sub">Others</li>
  </ul>
  <div class="side-btn">
    <svg width="22" height="18" viewBox="0 0 20 18"><path d="M1 6h18l-2 11H3z" fill="#fff"/><path d="M6 6l4-5 4 5" stroke="#fff" stroke-width="2" fill="none"/></svg>My Cart - 0 items
  </div>
  <div class="side-btn">
    <svg width="18" height="18" viewBox="0 0 18 18"><rect x="1" y="9" width="4" height="8" fill="#fff"/><rect x="7" y="3" width="4" height="14" fill="#fff"/><rect x="13" y="6" width="4" height="11" fill="#fff"/></svg>Compare Products
  </div>
  <div class="side-offer" role="img" aria-label="Offer photo: shopper carrying a basket of groceries in a supermarket aisle">
    <div class="badge">50%</div>
    <div class="text">Hurry offer<span>ends soon</span></div>
  </div>
  <h3 class="side-title spaced" style="font-weight:400">Latest Products</h3>
  <div class="mini-product">
    <div class="mini-thumb" role="img" aria-label="Red snapper fillets" style="background:linear-gradient(135deg,#e9a6a6,#c45d63)"></div>
    <div class="mini-info">Red Snapper (1kg)<div class="price">$1,000.00</div>
      <svg width="18" height="16" viewBox="0 0 20 18"><path d="M1 6h18l-2 11H3z" fill="#333"/><path d="M6 6l4-5 4 5" stroke="#333" stroke-width="2" fill="none"/></svg>
    </div>
  </div>
  <div class="mini-product" style="padding-top:20px">
    <div class="mini-thumb" role="img" aria-label="Whole red snapper fish" style="background:linear-gradient(135deg,#e8e8e8,#8a8f94)"></div>
    <div class="mini-info">Red Snapper (1kg)<div class="price">$1,000.00</div>
      <svg width="18" height="16" viewBox="0 0 20 18"><path d="M1 6h18l-2 11H3z" fill="#333"/><path d="M6 6l4-5 4 5" stroke="#333" stroke-width="2" fill="none"/></svg>
    </div>
  </div>
</aside>

<main class="abs main">
  <section class="latest">
    <div class="section-head"><h2>Latest Products</h2><span class="next-btn"><svg width="10" height="14" viewBox="0 0 10 14"><path d="M2 1l6 6-6 6" stroke="#fff" stroke-width="2.5" fill="none"/></svg></span></div>
    <div class="product-grid">
      <article class="product-card"><div class="product-photo" role="img" aria-label="Fresh blueberries" style="background:linear-gradient(135deg,#4a3f35,#2e3650 50%,#4b5a7d)"></div><div class="product-name">Cras accumsan felis</div><div class="product-price">$1,000.00</div></article>
      <article class="product-card"><div class="product-photo" role="img" aria-label="Basket of mixed vegetables" style="background:linear-gradient(135deg,#c0742a,#6a8a2e 50%,#b2322a)"></div><div class="product-name">Cras accumsan felis</div><div class="product-price">$1,000.00</div></article>
      <article class="product-card"><div class="product-photo" role="img" aria-label="Whole fish on a wooden board" style="background:linear-gradient(135deg,#cfc7b6,#8d8c86 55%,#b9a98c)"></div><div class="product-name">Cras accumsan felis</div><div class="product-price">$1,000.00</div></article>
    </div>
    <div class="offer-strip">
      <div class="offer-tile offer-ship" role="img" aria-label="Free shipping banner with delivery man carrying a box">
        <h3>Free Shipping</h3><p>On order over $30 offer today</p>
      </div>
      <div class="offer-tile offer-call" role="img" aria-label="Call banner with woman on a phone">
        <h3>Give us call</h3><p>1-800-Pantrys<br>(1-800-726-8797)</p>
      </div>
    </div>
  </section>

  <section class="featured">
    <div class="section-head"><h2>Featured Products</h2><span class="next-btn"><svg width="10" height="14" viewBox="0 0 10 14"><path d="M2 1l6 6-6 6" stroke="#fff" stroke-width="2.5" fill="none"/></svg></span></div>
    <div class="product-grid" style="margin-top:3px">
      <article class="product-card"><div class="product-photo" role="img" aria-label="Grilled steaks" style="background:linear-gradient(135deg,#2a1a12,#7a3a1e 55%,#3a2a1e)"></div><div class="product-name">Cras accumsan felis</div><div class="product-price">$1,000.00</div></article>
      <article class="product-card"><div class="product-photo" role="img" aria-label="Pasta on a fork" style="background:linear-gradient(135deg,#1e1e1e,#4a4a4a 45%,#d9822b 70%,#2a2a2a)"></div><div class="product-name">Cras accumsan felis</div><div class="product-price">$1,000.00</div></article>
      <article class="product-card"><div class="product-photo" role="img" aria-label="Bundle of fresh asparagus" style="background:linear-gradient(135deg,#8a8478,#6f8a3a 50%,#d8d0c0)"></div><div class="product-name">Cras accumsan felis</div><div class="product-price">$1,000.00</div></article>
      <article class="product-card"><div class="product-photo" role="img" aria-label="Assorted groceries and bottles" style="background:linear-gradient(135deg,#f4efe2,#c9a24a 45%,#7a9a3a 75%,#f2eee4)"></div><div class="product-name">Cras accumsan felis</div><div class="product-price">$1,000.00</div></article>
      <article class="product-card"><div class="product-photo" role="img" aria-label="Strawberries and berries on wood" style="background:linear-gradient(135deg,#9a6a46,#c0303a 50%,#5a2a4a)"></div><div class="product-name">Cras accumsan felis</div><div class="product-price">$1,000.00</div></article>
      <article class="product-card"><div class="product-photo" role="img" aria-label="Basket of vegetables with carrots" style="background:linear-gradient(135deg,#5a3a20,#b0481e 50%,#6a8a2e)"></div><div class="product-name">Cras accumsan felis</div><div class="product-price">$1,000.00</div></article>
      <article class="product-card"><div class="product-photo" role="img" aria-label="Fresh fish with lemon" style="background:linear-gradient(135deg,#f2f2f2,#9aa0a4 55%,#e6e6e6)"></div><div class="product-name">Cras accumsan felis</div><div class="product-price">$1,000.00</div></article>
      <article class="product-card"><div class="product-photo" role="img" aria-label="Salmon fillet on a board" style="background:linear-gradient(135deg,#6a4a32,#e8704a 50%,#5a3e2a)"></div><div class="product-name">Cras accumsan felis</div><div class="product-price">$1,000.00</div></article>
      <article class="product-card"><div class="product-photo" role="img" aria-label="Grilled shrimp skewers" style="background:linear-gradient(135deg,#e9d4b0,#c85a30 50%,#f2f0ea)"></div><div class="product-name">Cras accumsan felis</div><div class="product-price">$1,000.00</div></article>
    </div>
  </section>
</main>

<section class="abs wide-banner" role="img" aria-label="Advert banner with plated dish and salmon on dark background">
  <div class="art"></div>
  <div class="line">Phasellus et <b>pulvinar</b> tellus accumsan.</div>
  <div class="cta"><svg width="12" height="12" viewBox="0 0 12 12"><circle cx="6" cy="6" r="6" fill="#1c1c1c"/><path d="M5 3l3 3-3 3" stroke="#fff" stroke-width="1.6" fill="none"/></svg>Learn More</div>
</section>

<footer class="abs site-footer">
  <div class="footer-col nav-menu" style="left:130px">
    <h4>Navigation Menu</h4>
    <ul><li>All</li><li>Health &amp; Wellness</li><li>Fruits &amp; Vegs</li><li>Poultry, Meat &amp; Fish</li><li>Food Stuffs</li><li>Recipes</li><li>Others</li></ul>
  </div>
  <div class="footer-col" style="left:422px">
    <h4>Customer Service</h4>
    <ul><li>About Us</li><li>Delivery Information</li><li>Privacy Policy</li><li>Term &amp; Condition</li></ul>
  </div>
  <div class="footer-col" style="left:726px">
    <h4>My Account</h4>
    <ul><li>My Product</li><li>My Orders</li><li>My Address</li><li>My Personal Info</li></ul>
  </div>
  <div class="footer-col" style="left:956px">
    <h4>Other Links</h4>
    <ul><li>Site Map</li><li>Search Terms</li><li>Advanced Search</li><li>Orders and Returns</li><li>Contact Us</li></ul>
  </div>
  <div class="socials">
    <span></span><span></span><span></span>
    <span><svg width="16" height="12" viewBox="0 0 16 12"><rect x="1" y="1" width="14" height="10" fill="none" stroke="#555" stroke-width="1.5"/><path d="M1 1l7 6 7-6" stroke="#555" stroke-width="1.5" fill="none"/></svg></span>
    <span></span>
  </div>
  <div class="payments">
    <span>PayLink</span><span>Roam</span><span>Vera Spark</span><span>Vera</span>
  </div>
</footer>
<div class="abs copyright">Copyright © 2014 Pantrybasket.example Ltd. All rights reserved.</div>

</body>
</html>
```